Birch Ledger brochure to showcase Masonry, landscape and concrete services

SEE RECENT COMMENT PAGE FOR BEST INFO We need a brochure designed to help inform our clients of our services and give them information on the pitfalls in the masonry, landscape and Hardscape industry, including drainage and frost protection, showcase some of our work we like to make all our material for marketing geared toward helping the client learn something. Drainage on any site is the number one component to a successful landscape, Hardscape and outdoor living area. This is often and overlooked to get to the stuff that's fun in turn, causing failure from frost due to northern Minnesota's harsh climate. Creating many disappointments on a large investment project. The brochure should also have a section focused on masonry, including fireplaces chimney repair, stucco repair, stone and brick. Some of the language should be editable. I will attach pictures and our logo.

Target Market(s)

Older customers with dual income looking to update and add outdoor living

Industry/Entity Type

Masonry, landscape, concrete, outdoor living

Font styles to use
Serif
Sans Serif
Other font styles liked:
• Arial

Colors

Designer to choose only greyscale colors for use in the design.

Requirements
Must have
• I really like gray, silver and black when I do marketing mixed with White, but I thought adding some greenery for the landscape portion might look good too on this brochure
Nice to have
• I do not like it too busy so keep it clean and simple
Should not have
• Tons of clutter, tons of words, hard to read and look at

```html
<!DOCTYPE html>
<html lang="en">
<head>
<meta charset="UTF-8">
<title>Birch Ledger Brochure</title>
<link rel="stylesheet" href="https://fonts.googleapis.com/css2?family=Poppins:wght@300;400;500;700&display=swap">
<style>
  :root {
    --bg: #e4e4e4;
    --ink: #111111;
    --black: #161616;
    --charcoal: #2a2a2a;
    --grey: #6d6d6d;
    --silver: #d9d9d9;
    --paper: #f7f7f7;
    --white: #ffffff;
  }
  * { box-sizing: border-box; margin: 0; padding: 0; }
  html, body { width: 720px; height: 1200px; overflow: hidden; }
  body {
    background: var(--bg);
    font-family: "Poppins", Arial, sans-serif;
    color: var(--ink);
    position: relative;
  }
  .spread {
    position: absolute;
    left: 0;
    width: 720px;
    height: 556px;
    overflow: hidden;
    box-shadow: 0 6px 18px rgba(0,0,0,0.18);
  }
  .spread--outside { top: 28px; background: var(--paper); }
  .spread--inside {
    top: 616px;
    background: linear-gradient(115deg, var(--white) 0%, #f1f1f1 45%, #e3e3e3 100%);
  }
  .fold {
    position: absolute; top: 0; bottom: 0; width: 1px;
    background: rgba(0,0,0,0.08);
  }
  .fold--first { left: 240px; }
  .fold--second { left: 480px; }
  .photo { position: absolute; }

  /* outside spread */
  .intro-panel {
    position: absolute; left: 0; top: 0; width: 250px; height: 556px;
    background: var(--black);
    clip-path: polygon(0 0, 100% 0, 92% 100%, 0 100%);
  }
  .intro-copy {
    position: absolute; left: 26px; top: 34px; width: 196px; color: var(--white);
  }
  .intro-copy h1 {
    font-size: 15px; font-weight: 700; line-height: 1.2; text-transform: uppercase;
    margin-bottom: 12px;
  }
  .intro-copy p { font-size: 8.6px; font-weight: 300; line-height: 1.5; margin-bottom: 10px; }
  .photo--ridge {
    left: 0; top: 218px; width: 250px; height: 190px;
    background: linear-gradient(160deg, #b9b3a3 0%, #7d7a5a 45%, #4f5a3a 100%);
    clip-path: polygon(0 0, 100% 46%, 100% 100%, 0 62%);
  }
  .photo--fireplace {
    left: 0; top: 336px; width: 250px; height: 220px;
    background: linear-gradient(150deg, #a07a52 0%, #6e6258 50%, #3f4a44 100%);
    clip-path: polygon(0 0, 100% 40%, 100% 100%, 0 100%);
  }
  .photo--patio-forms {
    left: 228px; top: 0; width: 252px; height: 336px;
    background: linear-gradient(180deg, #2e3440 0%, #5a5552 45%, #7a5a52 100%);
    clip-path: polygon(10% 0, 100% 0, 100% 96%, 0 88%);
  }
  .contact-box {
    position: absolute; left: 238px; top: 318px; width: 232px; height: 238px;
    background: var(--black); color: var(--white);
    clip-path: polygon(0 0, 100% 7%, 100% 100%, 0 100%);
    padding: 34px 18px 0 20px;
  }
  .contact-box h2 { font-size: 10px; font-weight: 300; text-align: center; margin-bottom: 10px; }
  .contact-box .lead { font-size: 7px; font-style: italic; font-weight: 300; text-align: center; line-height: 1.45; margin-bottom: 16px; }
  .contact-list { list-style: none; }
  .contact-list li {
    display: flex; align-items: center; gap: 8px;
    font-size: 10px; font-weight: 500; margin-bottom: 12px;
  }
  .contact-list svg { width: 11px; height: 11px; flex: none; }
  .photo--firepit {
    left: 490px; top: 8px; width: 222px; height: 320px;
    background: linear-gradient(180deg, #2f4a22 0%, #4c6b34 45%, #6f6a64 75%, #8a857f 100%);
    clip-path: polygon(0 0, 100% 0, 100% 88%, 6% 100%);
  }
  .cover-panel {
    position: absolute; left: 480px; top: 0; width: 240px; height: 556px;
    background: linear-gradient(160deg, var(--white) 40%, var(--silver) 100%);
  }
  .brand {
    position: absolute; display: flex; flex-direction: column; align-items: center;
    color: var(--grey);
  }
  .brand-mark { width: 34px; height: 34px; border-radius: 50%; background: var(--grey); margin-bottom: 10px; }
  .brand-name { font-size: 19px; font-weight: 300; letter-spacing: 0.18em; text-transform: uppercase; }
  .brand-tagline { font-size: 7.5px; font-weight: 300; letter-spacing: 0.28em; margin-top: 4px; }
  .brand--cover { left: 480px; top: 400px; width: 240px; }

  /* inside spread */
  .ghost-band {
    position: absolute; background: rgba(255,255,255,0.55);
    left: 160px; top: 0; width: 280px; height: 556px;
    clip-path: polygon(30% 0, 100% 0, 60% 100%, 0 100%);
  }
  .about { position: absolute; }
  .about h2 {
    font-size: 14px; font-weight: 700; line-height: 1.15; text-transform: uppercase; color: var(--ink);
  }
  .about h2 span { display: block; font-weight: 400; color: var(--grey); }
  .about p { font-size: 8.2px; line-height: 1.45; margin-top: 10px; color: var(--charcoal); }
  .about--long { left: 30px; top: 34px; width: 196px; }
  .about--short { left: 300px; top: 300px; width: 230px; }
  .photo--house {
    left: 0; top: 346px; width: 232px; height: 210px;
    background: linear-gradient(160deg, #9fb3c4 0%, #55606a 50%, #6b4a3a 100%);
    clip-path: polygon(0 18%, 52% 0, 100% 34%, 100% 100%, 0 100%);
  }
  .photo--kitchen {
    left: 282px; top: 40px; width: 438px; height: 300px;
    background: linear-gradient(170deg, #2f4526 0%, #4d6a38 30%, #8c8780 60%, #b4aea6 100%);
    clip-path: polygon(8% 0, 100% 10%, 100% 100%, 34% 86%, 0 40%);
  }
  .photo--drainage {
    left: 556px; top: 330px; width: 164px; height: 226px;
    background: linear-gradient(165deg, #6a6460 0%, #7a5848 55%, #4f3a30 100%);
    clip-path: polygon(26% 0, 100% 14%, 100% 100%, 0 100%, 0 30%);
  }
</style>
</head>
<body>

<section class="spread spread--outside">
  <div class="cover-panel"></div>

  <div class="intro-panel"></div>
  <div class="photo photo--ridge" role="img" aria-label="Photo of a hillside landscape with native plantings and distant forest"></div>
  <div class="photo photo--fireplace" role="img" aria-label="Photo of a cabin living room with a stacked stone fireplace"></div>
  <div class="intro-copy">
    <h1>Building Excellence<br>One Stone at a Time</h1>
    <p>Explore the rich history and meticulous craftsmanship behind every stone laid by Birch Ledger in Pine Harbor, MN. Let our passion for masonry elevate your next project.</p>
    <p>Your vision, realized with our expertise.</p>
  </div>

  <div class="photo photo--patio-forms" role="img" aria-label="Photo of a new paver patio being formed beneath a raised deck"></div>

  <div class="contact-box">
    <h2>Get in Touch with Birch Ledger!</h2>
    <p class="lead">Have a question? Want to discuss your next project? You're in the right place! Don't hesitate to reach out, Birch Ledger is here to help!</p>
    <ul class="contact-list">
      <li>
        <svg viewBox="0 0 24 24" aria-hidden="true"><rect x="2" y="5" width="20" height="14" rx="2" fill="none" stroke="#fff" stroke-width="2"/><path d="M2 6l10 7 10-7" fill="none" stroke="#fff" stroke-width="2"/></svg>
        birchledger24@example.com
      </li>
      <li>
        <svg viewBox="0 0 24 24" aria-hidden="true"><path d="M6 2h4l2 5-3 2a11 11 0 0 0 6 6l2-3 5 2v4a2 2 0 0 1-2 2A18 18 0 0 1 4 4a2 2 0 0 1 2-2z" fill="#fff"/></svg>
        (555) 014-2286
      </li>
      <li>
        <svg viewBox="0 0 24 24" aria-hidden="true"><circle cx="12" cy="12" r="10" fill="none" stroke="#fff" stroke-width="2"/><path d="M2 12h20M12 2c3 3 3 17 0 20M12 2c-3 3-3 17 0 20" fill="none" stroke="#fff" stroke-width="1.5"/></svg>
        www.birchledgerstudio.com
      </li>
    </ul>
  </div>

  <div class="photo photo--firepit" role="img" aria-label="Photo of a flagstone patio with a fire pit and wooden chairs among trees"></div>
  <div class="brand brand--cover">
    <div class="brand-mark"></div>
    <div class="brand-name">Birch Ledger</div>
    <div class="brand-tagline">Built For Every Season</div>
  </div>

  <div class="fold fold--first"></div>
  <div class="fold fold--second"></div>
</section>

<section class="spread spread--inside">
  <div class="ghost-band"></div>

  <div class="about about--long">
    <h2>Long version of <span>who we are</span></h2>
    <p>Birch Ledger is a masonry and landscape company serving northern Minnesota and Wisconsin. We are dedicated to giving our clients exactly what they expect—every time. To protect every project and investment, we focus on educating clients and helping them understand potential pitfalls during the planning stage. In our harsh climate, drainage, frost protection, and water mitigation are critical and often overlooked, leading to costly disappointments later. The foundation of every project is the most important part, every time. We specialize in masonry, landscape services, and outdoor living spaces.</p>
    <p>Birch Ledger builds outdoor spaces for every season with craftsmanship that lasts.</p>
  </div>
  <div class="photo photo--house" role="img" aria-label="Photo of a modern home with a stone retaining wall and plantings"></div>

  <div class="photo photo--kitchen" role="img" aria-label="Photo of an outdoor kitchen with stone veneer island on a stone patio"></div>

  <div class="about about--short">
    <h2>Short version of <span>who we are</span></h2>
    <p>Birch Ledger is a masonry and landscape company serving northern Minnesota and Wisconsin. We help clients get exactly what they expect by focusing on smart planning and educating them before work begins. In a harsh climate, proper drainage, frost protection, and water control are essential to protect any outdoor investment.</p>
    <p>Specializing in masonry, landscaping, and outdoor living spaces, Birch Ledger builds for every season with craftsmanship made to last.</p>
  </div>

  <div class="photo photo--drainage" role="img" aria-label="Photo of a drainage pipe being laid in an excavated trench"></div>

  <div class="fold fold--first"></div>
  <div class="fold fold--second"></div>
</section>

</body>
</html>
```